Statement of Qualifications Brochure for Civil/Construction Engineering Company

We need a "statement of qualification" pdf brochure with the content that is attached and in conjuncture to the new logo we are building. We also need a logo re-design (hi-rez and color) for the logo attached.

This brochure will be sent out to companies that require information of what our company does, or for requirements in services.

We would like a black and 'runway airport blue' color scheme for the brochure and the logo. It should appear professional, easy to read, and informative.

Reason: Hello, We realize our answers to some of your questions did not come to you promptly, so we have extended this deadline by 5 days. Thank you all!

Target Market(s)

Apartment Complex ownership companies. These companies typically own 10-50 mulit-unit complexes.

Industry/Entity Type

Airport

Font styles to use
Other font styles liked:
• Would like a professional, non-decorative font

Requirements
Must have
• Sharp and easy to read. Focus on information.
Nice to have
• Nice photos, we have other photos we can send to insert if necessary

```html
<!DOCTYPE html>
<html lang="en">
<head>
<meta charset="utf-8">
<title>Statement of Qualifications – Environmental Due Diligence</title>
<link href="https://fonts.googleapis.com/css2?family=Raleway:wght@300;400;500;700&display=swap" rel="stylesheet">
<style>
  :root {
    --ink: #000000;
    --paper: #ffffff;
    --runway-blue: #1fa3e0;
    --header-grey: #8a8f94;
    --photo-sky: #9ec3dd;
    --photo-concrete: #c9c4ba;
    --photo-timber: #b08a5a;
    --photo-soil: #7a5a3e;
  }
  * { margin: 0; padding: 0; box-sizing: border-box; }
  html, body { width: 848px; height: 1200px; overflow: hidden; background: var(--ink); }
  .page {
    position: relative; width: 848px; height: 1200px; overflow: hidden;
    background: var(--ink); font-family: "Raleway", Arial, sans-serif; color: var(--paper);
  }
  .hero-photo {
    position: absolute; left: 0; top: 0; width: 848px; height: 528px;
    background: linear-gradient(180deg, var(--photo-sky) 0%, #c4d3dc 22%, var(--photo-concrete) 45%, #b9a88e 70%, var(--photo-soil) 100%);
  }
  .hero-photo::after {
    content: ""; position: absolute; inset: 0;
    background: linear-gradient(90deg, rgba(176,138,90,.55) 0%, rgba(176,138,90,.35) 45%, rgba(230,228,222,.35) 55%, rgba(122,90,62,.45) 100%);
  }
  .running-head {
    position: absolute; left: 52px; top: 25px; font-size: 13px; color: var(--header-grey);
    letter-spacing: .2px;
  }
  .running-head strong { font-weight: 700; }
  .running-head .firm { color: var(--runway-blue); }
  .thumb { position: absolute; left: 54px; width: 244px; }
  .thumb-crew { top: 573px; height: 138px; background: linear-gradient(135deg, #c98a55, #9b9a92 55%, #6d6a62); }
  .thumb-rebar { top: 721px; height: 139px; background: linear-gradient(160deg, #5e5f5c, #8b8c88 50%, #3f403e); }
  .section-title {
    position: absolute; left: 305px; top: 566px; font-weight: 300; font-size: 31px;
    color: var(--runway-blue); letter-spacing: .3px; line-height: 1;
  }
  .service-list {
    position: absolute; left: 306px; top: 603px; list-style: none;
    font-size: 13px; font-weight: 500; line-height: 21px; text-transform: uppercase;
  }
  .service-list li::before { content: "• "; }
  .body-copy {
    position: absolute; top: 752px; width: 235px; font-size: 12.4px; line-height: 21.9px;
    text-align: justify; letter-spacing: -.1px;
  }
  .body-copy p + p { margin-top: 22px; }
  .col-left { left: 306px; }
  .col-right { left: 559px; width: 238px; }
  .footer-contact {
    position: absolute; left: 53px; top: 1158px; font-size: 12.5px; color: var(--runway-blue);
  }
  .footer-contact strong { font-weight: 700; }
  .page-number { position: absolute; left: 789px; top: 1158px; font-size: 12.5px; color: var(--header-grey); }
  .accent-lines { position: absolute; left: 0; top: 0; pointer-events: none; }
</style>
</head>
<body>
<div class="page">
  <div class="hero-photo" role="img" aria-label="Construction site with a finished concrete wall beside rebar and timber formwork under a blue sky"></div>

  <div class="running-head">Statement of <strong>QUALIFICATIONS</strong> • <span class="firm">KESTREL CIVIL, PLLC</span></div>

  <div class="thumb thumb-crew" role="img" aria-label="Crew in safety vests and hard hats working on a formed foundation wall"></div>
  <div class="thumb thumb-rebar" role="img" aria-label="Close view of tied reinforcing steel bars"></div>

  <h1 class="section-title">ENVIRONMENTAL DUE DILIGENCE</h1>
  <ul class="service-list">
    <li>Phase I Environmental Site Assessments (ESA)</li>
    <li>Environmental Transaction Screens</li>
    <li>Vapor Intrusion and Encroachment Assessments</li>
    <li>Record Searches and Risk Assessments</li>
    <li>Historical Environmental Reports</li>
    <li>Environmental Database Reports</li>
  </ul>

  <div class="body-copy col-left">
    <p>ASTM Standard E1527-13, “Environmental Site Assessments: Phase I Environmental Site Assessment Process” is the Standard Practice used for most Phase I environmental assessments. A typical ESA has three major components: research, investigation, and evaluation. Research includes the review and analysis of as much environmental data as possible about the site and any adjacent or nearby properties. Investigation involves a thorough visual assessment of the property and a cursory off-site visual assessment of adjacent properties. We observe all mechanical, electrical, and maintenance and storage areas where hazardous materials might be used and hazardous wastes may have been spilled, stored, or disposed.</p>
  </div>
  <div class="body-copy col-right">
    <p>The evaluation of the information collected during the research and investigation process is critical to understanding the environmental condition of the site, and if adjacent or nearby properties present an environmental concern or recognized environmental condition.</p>
    <p>This is where our staff of Environmental Professionals steps in. They have extensive experience with most types of commercial and industrial properties and environmental conditions. Our Reports are accurate and easy to understand, and always provide our Clients with the assurance they need to move forward with their projects.</p>
  </div>

  <div class="footer-contact">Dallas, TX • <strong>214.555.0142</strong></div>
  <div class="page-number">5</div>

  <svg class="accent-lines" width="848" height="1200" viewBox="0 0 848 1200" aria-hidden="true">
    <g stroke-width="1.4" fill="none">
      <line x1="605" y1="210" x2="820" y2="0" stroke="var(--runway-blue)"/>
      <line x1="496" y1="497" x2="848" y2="185" stroke="var(--runway-blue)"/>
      <line x1="472" y1="128" x2="848" y2="482" stroke="var(--paper)"/>
      <line x1="582" y1="357" x2="848" y2="620" stroke="var(--paper)"/>
      <line x1="0" y1="385" x2="103" y2="487" stroke="var(--paper)"/>
    </g>
  </svg>
</div>
</body>
</html>
```